Flyer informing about the activities of people in action

Wege im Wandel (www.wegeimwandel-beratung.ch) offers coaching, medation, support for traumatized people and conflict and crisis intervention. The flyer should inform about the activities in a plain and simple way (see logo on the homepage).

Target Market(s)

Adults who live in Switzerland or Germany

Requirements
Must have
• - simple flyer, the design is based on my logo. Brief information about my offer, reference to my homepage www.wegeimwandel-beratung.
- 2-sided: on the first page - fire circle with text (see homepage - Home), on the back - offer with logo
- possibly a square flyer

Should not have
• no photos

```html
<!DOCTYPE html>
<html lang="en">
<head>
<meta charset="utf-8">
<title>Wege im Wandel – Flyer</title>
<link rel="stylesheet" href="https://fonts.googleapis.com/css2?family=Raleway:wght@400;500;700;800&family=Poppins:wght@400;600;700&display=swap">
<style>
  :root {
    --stage: #5f5f5f;
    --paper: #ffffff;
    --gold: #c9a500;
    --gold-deep: #a3860a;
    --gold-light: #e2c43a;
    --ink: #222222;
    --ink-soft: #444444;
    --brand: #9a7a4a;
  }
  * { box-sizing: border-box; margin: 0; padding: 0; }
  html, body { width: 1200px; height: 764px; overflow: hidden; background: var(--stage); }
  .canvas { position: relative; width: 1200px; height: 764px; }
  .flyer {
    position: absolute; top: 115px; width: 535px; height: 535px;
    background: var(--paper); overflow: hidden;
  }
  .flyer--front { left: 43px; }
  .flyer--back { left: 612px; }
  .flyer svg.waves { position: absolute; inset: 0; width: 535px; height: 535px; }

  /* front */
  .quote-mark {
    position: absolute; font-family: "Raleway", sans-serif; font-weight: 800;
    color: var(--gold); font-size: 96px; line-height: 1;
  }
  .quote-mark--open { left: 24px; top: 40px; }
  .quote-mark--close { left: 326px; top: 334px; }
  .headline {
    position: absolute; left: 92px; top: 64px;
    font-family: "Raleway", sans-serif; font-weight: 700; font-size: 63px;
    color: var(--gold); line-height: 1; white-space: nowrap;
  }
  .needs {
    position: absolute; left: 26px; top: 136px;
    font-family: "Raleway", sans-serif; font-weight: 700; font-size: 31.5px;
    color: var(--ink); line-height: 40px; white-space: nowrap;
  }
  .benefit {
    position: absolute; right: 30px; top: 248px;
    font-family: "Raleway", sans-serif; font-weight: 700; font-size: 37px;
    color: var(--gold); line-height: 1; white-space: nowrap;
  }
  .context {
    position: absolute; left: 26px; top: 294px;
    font-family: "Raleway", sans-serif; font-weight: 400; font-size: 27px;
    color: var(--ink-soft); line-height: 34px; white-space: nowrap;
  }
  .cta {
    position: absolute; left: 285px; top: 458px; width: 133px; height: 31px;
    border-radius: 16px; background: linear-gradient(var(--gold-light), var(--gold-deep));
    color: #fff; font-family: "Raleway", sans-serif; font-weight: 800; font-size: 18px;
    display: flex; align-items: center; justify-content: center;
  }
  .website {
    position: absolute; left: 190px; top: 496px; display: flex; align-items: center; gap: 8px;
    font-family: "Raleway", sans-serif; font-weight: 700; font-size: 19px; color: var(--ink-soft);
    white-space: nowrap;
  }

  /* back */
  .offer-title {
    position: absolute; left: 142px; top: 22px; width: 250px; height: 46px;
    border-radius: 23px; background: linear-gradient(var(--gold-light), var(--gold-deep));
    color: #fff; font-family: "Poppins", sans-serif; font-weight: 700; font-size: 33px;
    display: flex; align-items: center; justify-content: center; letter-spacing: 0.5px;
  }
  .divider { position: absolute; left: 266px; top: 92px; width: 2px; height: 174px; background: var(--gold-deep); }
  .service { position: absolute; width: 200px; }
  .service__icon {
    position: absolute; left: -70px; top: 0; width: 58px; height: 58px; border-radius: 50%;
    background: var(--gold); box-shadow: 0 3px 6px rgba(0,0,0,0.15);
  }
  .service__name {
    font-family: "Poppins", sans-serif; font-weight: 600; font-size: 12.5px; color: var(--ink);
    line-height: 15px; margin-bottom: 3px;
  }
  .service__text {
    font-family: "Poppins", sans-serif; font-weight: 400; font-size: 7.6px; color: var(--ink-soft);
    line-height: 10.5px; width: 135px;
  }
  .service--coaching { left: 120px; top: 93px; }
  .service--trauma { left: 120px; top: 175px; }
  .service--mediation { left: 375px; top: 92px; }
  .service--crisis { left: 375px; top: 175px; }
  .brand {
    position: absolute; left: 205px; top: 440px; display: flex; align-items: center; gap: 12px;
  }
  .brand__dot { width: 20px; height: 20px; border-radius: 50%; background: var(--brand); flex: none; }
  .brand__name {
    font-family: "Raleway", sans-serif; font-weight: 500; font-size: 34px; color: var(--brand);
    white-space: nowrap; line-height: 1;
  }
</style>
</head>
<body>
<main class="canvas">

  <section class="flyer flyer--front">
    <svg class="waves" viewBox="0 0 535 535" aria-hidden="true">
      <defs>
        <linearGradient id="goldFront" x1="0" y1="0" x2="1" y2="1">
          <stop offset="0" stop-color="#d9b81c"/>
          <stop offset="1" stop-color="#9c800a"/>
        </linearGradient>
      </defs>
      <path d="M150 0 H535 V170 C500 90 420 30 300 22 C230 18 180 12 150 0 Z" fill="url(#goldFront)"/>
      <path d="M290 0 H535 V110 C510 50 440 12 290 0 Z" fill="#a98c0c"/>
      <path d="M0 395 C90 440 170 470 280 465 C390 460 470 420 535 395 V535 H0 Z" fill="url(#goldFront)"/>
      <path d="M0 432 C110 480 230 500 330 490 C420 480 490 450 535 430 V535 H0 Z" fill="#fff"/>
      <path d="M0 445 C110 492 230 512 330 502 C420 492 490 462 535 442 V535 H0 Z" fill="url(#goldFront)"/>
      <path d="M0 470 C140 520 300 530 535 500 V535 H0 Z" fill="#fff"/>
    </svg>
    <span class="quote-mark quote-mark--open">“</span>
    <h1 class="headline">You want</h1>
    <p class="needs">Solve your stressful situation.<br>Clarify your important questions.</p>
    <p class="benefit">get ahead easier</p>
    <p class="context">in the frustrating collaboration or your<br>laborious life (together).</p>
    <span class="quote-mark quote-mark--close">”</span>
    <a class="cta">VISIT NOW!</a>
    <p class="website">
      <svg width="18" height="18" viewBox="0 0 20 20" aria-hidden="true">
        <circle cx="10" cy="10" r="9" fill="none" stroke="#b8960a" stroke-width="2"/>
        <ellipse cx="10" cy="10" rx="4" ry="9" fill="none" stroke="#b8960a" stroke-width="1.6"/>
        <line x1="1" y1="10" x2="19" y2="10" stroke="#b8960a" stroke-width="1.6"/>
      </svg>
      www.wegeimwandel-beratung
    </p>
  </section>

  <section class="flyer flyer--back">
    <svg class="waves" viewBox="0 0 535 535" aria-hidden="true">
      <defs>
        <linearGradient id="goldBack" x1="0" y1="0" x2="1" y2="1">
          <stop offset="0" stop-color="#d9b81c"/>
          <stop offset="1" stop-color="#9c800a"/>
        </linearGradient>
      </defs>
      <g stroke="#c9a500" stroke-width="1.5">
        <line x1="25" y1="40" x2="140" y2="40"/><line x1="25" y1="46" x2="140" y2="46"/><line x1="25" y1="52" x2="140" y2="52"/>
        <line x1="394" y1="40" x2="510" y2="40"/><line x1="394" y1="46" x2="510" y2="46"/><line x1="394" y1="52" x2="510" y2="52"/>
      </g>
      <path d="M0 245 C60 290 130 350 230 352 C330 354 420 280 535 262 V535 H0 Z" fill="url(#goldBack)"/>
      <path d="M0 330 C90 350 180 360 270 320 C360 285 450 280 535 300 V535 H0 Z" fill="#fff"/>
      <path d="M0 345 C90 365 190 372 275 335 C360 300 450 296 535 312 V360 C440 330 350 340 270 385 C190 430 90 420 0 395 Z" fill="url(#goldBack)"/>
      <path d="M0 395 C90 420 190 430 270 385 C350 340 440 330 535 360 V535 H0 Z" fill="#fff"/>
    </svg>
    <h2 class="offer-title">WE OFFER</h2>
    <div class="divider"></div>

    <article class="service service--coaching">
      <span class="service__icon" role="img" aria-label="Coaching icon: speaker at a board with listeners"></span>
      <h3 class="service__name">Coaching</h3>
      <p class="service__text">Sometimes you need a counterpart to clarify your own situation or to discover new perspectives and options for action.</p>
    </article>
    <article class="service service--trauma">
      <span class="service__icon" role="img" aria-label="Support icon: one person comforting another"></span>
      <h3 class="service__name">Support for<br>Traumatized&nbsp; People</h3>
      <p class="service__text">Their life often feels heavy, oppressive, and joyless. You have tried unsuccessfully to free yourself from this lack of contact and perspective.</p>
    </article>
    <article class="service service--mediation">
      <span class="service__icon" role="img" aria-label="Mediation icon: seated meditating figure"></span>
      <h3 class="service__name">Medation</h3>
      <p class="service__text">You can no longer resolve certain conflicts yourself. Few words ignite a bitter argument or create an icy silence.</p>
    </article>
    <article class="service service--crisis">
      <span class="service__icon" role="img" aria-label="Intervention icon: two figures facing each other"></span>
      <h3 class="service__name">Conflict and crisis<br>intervention</h3>
      <p class="service__text">It doesn't feel good anymore - what exactly can be unclear. The encounter is uncomfortable. Suitable words are missing or difficult to find.</p>
    </article>

    <div class="brand">
      <span class="brand__dot"></span>
      <span class="brand__name">Wege im Wandel</span>
    </div>
  </section>

</main>
</body>
</html>
```